Business Card Design

We are looking for a business card designed for our landscaping company. We do landscaping installation & Maintenance Services. We would like to see designs that have basic landscaping in background. We also think it is important to have both of our names and phone numbers on the card. We need something that stands out a little whether it is shape of the card or thickness or design.

Industry/Entity Type

Business

Contact Information for Business Card

Pale Ridge Yardworks, paleridgeyardworks@mailbrook.net, Dale Purvine 555-213-7690, Martin Kolbey 555-864-1037

```html
<!DOCTYPE html>
<html lang="en">
<head>
<meta charset="UTF-8">
<title>Pale Ridge Yardworks – Business Card</title>
<link href="https://fonts.googleapis.com/css2?family=Open+Sans:wght@400;600;700&display=swap" rel="stylesheet">
<style>
  :root {
    --page-bg: #e9e7e4;
    --card-white: #ffffff;
    --leaf-green: #8dc63f;
    --leaf-green-deep: #7cb82f;
    --pale-green: #b9dc8e;
    --mist-green: #dcefc6;
    --text-white: #ffffff;
  }
  html, body {
    margin: 0;
    padding: 0;
    width: 1200px;
    height: 800px;
    overflow: hidden;
    background: var(--page-bg);
    font-family: "Open Sans", Arial, sans-serif;
  }
  .canvas {
    position: relative;
    width: 1200px;
    height: 800px;
  }
  .business-card {
    position: absolute;
    left: 180px;
    top: 160px;
    width: 840px;
    height: 480px;
    background: var(--card-white);
    box-shadow: 0 10px 30px rgba(0,0,0,0.18);
    overflow: hidden;
  }
  .card-shapes {
    position: absolute;
    inset: 0;
    width: 840px;
    height: 480px;
  }
  .grass-art {
    position: absolute;
    left: 18px;
    top: 200px;
    width: 190px;
    height: 140px;
    background: radial-gradient(ellipse at 45% 90%, var(--pale-green) 0%, var(--mist-green) 55%, rgba(255,255,255,0) 78%);
  }
  .company-block {
    position: absolute;
    left: 250px;
    top: 52px;
  }
  .company-name {
    margin: 0;
    font-size: 36px;
    font-weight: 700;
    color: var(--pale-green);
    letter-spacing: 0.3px;
  }
  .company-email {
    display: flex;
    align-items: center;
    gap: 8px;
    margin-top: 6px;
    font-size: 18px;
    color: var(--pale-green);
  }
  .email-dot {
    width: 14px;
    height: 14px;
    border-radius: 50%;
    border: 2px solid var(--pale-green);
    box-sizing: border-box;
  }
  .contacts {
    position: absolute;
    left: 520px;
    top: 248px;
    color: var(--text-white);
  }
  .contact { margin-bottom: 16px; }
  .contact-name {
    font-size: 26px;
    font-weight: 700;
    line-height: 1.2;
  }
  .contact-phone {
    display: flex;
    align-items: center;
    gap: 8px;
    font-size: 24px;
    font-weight: 600;
    line-height: 1.3;
  }
  .phone-icon { width: 20px; height: 20px; }
</style>
</head>
<body>
<main class="canvas">
  <section class="business-card">
    <svg class="card-shapes" viewBox="0 0 840 480" aria-hidden="true">
      <path class="green-field" fill="var(--leaf-green)"
        d="M0,330 C170,200 470,150 700,200 C760,212 790,215 810,190 C822,175 832,170 840,170 L840,480 L0,480 Z"/>
      <path class="top-swoosh" fill="none" stroke="var(--mist-green)" stroke-width="5" stroke-linecap="round"
        d="M220,70 C330,20 520,30 640,110"/>
      <path class="bottom-swoosh" fill="none" stroke="var(--mist-green)" stroke-width="5" stroke-linecap="round"
        d="M450,390 C560,450 720,470 820,400"/>
    </svg>

    <div class="grass-art" role="img" aria-label="Pale green grass and plant silhouette"></div>

    <div class="company-block">
      <h1 class="company-name">Pale Ridge Yardworks</h1>
      <div class="company-email"><span class="email-dot"></span>paleridgeyardworks@mailbrook.net</div>
    </div>

    <div class="contacts">
      <div class="contact">
        <div class="contact-name">Dale Purvine</div>
        <div class="contact-phone">
          <svg class="phone-icon" viewBox="0 0 20 20" aria-hidden="true">
            <circle cx="10" cy="10" r="8.5" fill="none" stroke="#fff" stroke-width="1.6"/>
            <path d="M7,5.5 L8.6,5.5 L9.2,8 L8.2,8.9 C8.8,10.3 9.7,11.2 11.1,11.8 L12,10.8 L14.5,11.4 L14.5,13 C11,13.5 6.5,9 7,5.5 Z" fill="#fff"/>
          </svg>
          555-213-7690
        </div>
      </div>
      <div class="contact">
        <div class="contact-name">Martin Kolbey</div>
        <div class="contact-phone">
          <svg class="phone-icon" viewBox="0 0 20 20" aria-hidden="true">
            <circle cx="10" cy="10" r="8.5" fill="none" stroke="#fff" stroke-width="1.6"/>
            <path d="M7,5.5 L8.6,5.5 L9.2,8 L8.2,8.9 C8.8,10.3 9.7,11.2 11.1,11.8 L12,10.8 L14.5,11.4 L14.5,13 C11,13.5 6.5,9 7,5.5 Z" fill="#fff"/>
          </svg>
          555-864-1037
        </div>
      </div>
    </div>
  </section>
</main>
</body>
</html>
```